Hemp (cannabis) CBD Oil 3-page Blog website

The objective is 1) to look like professional/serious company, 2) to get investors excited about our Hemp business, 3) to get investor email and phone numbers and build a sense community. Potential investors should become excited that this is their “window of opportunity,” because VelLorim is made up of extraordinary people who all have made successful business before, that the location in Uruguay is a huge benefit, that we will become the biggest and best CBD-oil manufacturer in Latin America, and that we focus on all-legal medicinal CBD oil extracted from hemp.

Target Market(s)

Potential investors looking to invest between $30,000-$1,000,000 USD into a HEMP startup business, based in Uruguay, South America.

Industry/Entity Type

Business

Number of Pages Required

3 page

Font styles to use
Sans Serif

Requirements
Must have
• Three pages: Home, Members Only, News (blog).
• FOR MORE DETAIL SEE ATTACHED WORD REQUIREMENTS DOCUMENT.
Nice to have
• Uruguay colors: sky blue, golden sun. Medicinal. Legal. Mainstream. Hemp. Professional people. Opportunity/Money/Investor. Uruguay. Latin America. 1st to Market.
Should not have
• Marijuana (HEMP yes, marijuana NO), anything that looks illegal.

```html
<!DOCTYPE html>
<html lang="en">
<head>
<meta charset="utf-8">
<title>VelLorim – Home</title>
<link href="https://fonts.googleapis.com/css2?family=Lora:wght@400;700&family=Open+Sans:wght@400;600&family=Roboto+Condensed:wght@400&display=swap" rel="stylesheet">
<style>
  :root{
    --blue:#2a63b0;
    --blue-dark:#2160ad;
    --green:#1aa362;
    --green-bright:#22b573;
    --grey-band:#e6e6e6;
    --team-band:#e1f2f5;
    --ink:#222;
    --muted:#555;
    --line:#b8c4d4;
  }
  *{box-sizing:border-box;margin:0;padding:0}
  html,body{width:686px;height:1200px;overflow:hidden;background:#fff}
  body{font-family:"Open Sans",Arial,sans-serif;color:var(--ink)}
  .page{position:relative;width:686px;height:1200px;overflow:hidden}
  .abs{position:absolute}

  /* top bar */
  .topbar{left:0;top:0;width:686px;height:21px;background:var(--blue)}
  .social{top:3px;width:15px;height:15px;border-radius:50%;background:var(--green-bright)}
  .topbar-contact{top:4px;color:#fff;font-size:9px;display:flex;align-items:center;gap:4px}
  .topbar-contact.phone{font-size:10.5px}

  /* header */
  .header{left:0;top:21px;width:686px;height:51px;background:#fff}
  .brand{font-family:"Open Sans",sans-serif;font-weight:400;color:var(--blue);font-size:22px;letter-spacing:.2px}
  .nav{top:57px;font-family:"Lora",serif;font-size:7.5px;color:#333;display:flex}
  .nav a{color:inherit;text-decoration:none;padding:0 9px;border-left:1px solid #bbb;line-height:11px}
  .nav a:first-child{border-left:0;color:var(--blue);font-weight:700}

  /* hero */
  .hero{left:0;top:72px;width:686px;height:235px;background:
     radial-gradient(ellipse at 75% 45%,#5e6b3a 0%,rgba(60,55,45,0) 35%),
     linear-gradient(180deg,#3b3733 0%,#2a2622 60%,#1d1a17 100%)}
  .hero-title{left:91px;top:203px;font-family:"Roboto Condensed",sans-serif;color:#fff;font-size:18.5px;line-height:23px}
  .hero-arrow{top:183px;width:19px;height:16px;background:#5a5652;border:1px solid #888;display:flex;align-items:center;justify-content:center}

  /* section headings */
  .section-title{left:0;width:686px;text-align:center;font-family:"Lora",serif;color:var(--blue);font-size:16px}
  .title-rule{height:1px;background:var(--line)}
  .title-rule span{position:absolute;left:50%;top:-1px;width:40px;height:2px;margin-left:-20px;background:var(--blue)}

  .about-text{left:112px;top:358px;width:462px;text-align:center;font-family:Arial,sans-serif;font-size:6px;line-height:9.6px;color:#222}
  .btn{background:var(--green);color:#fff;font-family:"Lora",serif;font-size:8.5px;display:flex;align-items:center;justify-content:center;gap:6px}

  /* cannabidiol */
  .cbd-band{left:0;top:436px;width:686px;height:247px;background:var(--grey-band)}
  .cbd-intro{left:0;top:480px;width:686px;text-align:center;font-family:Arial,sans-serif;font-size:6px;color:#222}
  .feature{font-family:"Lora",serif;font-size:9px;color:#333}
  .feature.right{text-align:right}
  .cbd-brand{left:0;top:636px;width:686px;text-align:center;color:var(--blue);font-size:24px}
  .cbd-sub{left:0;top:664px;width:686px;text-align:center;color:var(--blue);font-family:"Lora",serif;font-size:13px}

  /* news */
  .news-thumb{width:77px;height:54px;border:1px solid #ddd}
  .news-title{font-family:"Lora",serif;font-weight:700;font-size:6.5px;color:#222}
  .news-date{font-size:6px;color:var(--blue);display:flex;align-items:center;gap:4px}
  .news-body{width:150px;font-family:Arial,sans-serif;font-size:5.6px;line-height:9.4px;color:#444}
  .news-body b{color:var(--blue);font-weight:400}

  /* team */
  .team-band{left:0;top:822px;width:686px;height:158px;background:var(--team-band)}
  .member{top:882px;width:79px}
  .member-photo{width:79px;height:69px;border:2px solid #fff;outline:1px solid #c7d6db}
  .member-name{margin-top:5px;text-align:center;font-family:"Lora",serif;font-weight:700;font-size:7px;color:#555}

  /* call to action */
  .cta{left:0;top:980px;width:686px;height:52px;background:var(--blue-dark)}
  .cta-text{left:94px;top:991px;font-family:"Lora",serif;color:#fff;font-size:12px;line-height:17px}
  .cta-btn{left:479px;top:992px;width:113px;height:30px;background:var(--green-bright);color:#fff;text-align:center;font-family:Arial,sans-serif}

  /* footer */
  .footer{left:0;top:1032px;width:686px;height:146px;background:
     radial-gradient(ellipse at 80% 30%,#2f4a2c 0%,rgba(0,0,0,0) 45%),
     linear-gradient(180deg,#1c2a1c,#141c14)}
  .footer-head{font-family:"Lora",serif;font-size:7.5px;color:#fff;padding-bottom:4px;border-bottom:1px solid #6c7a6c}
  .footer-list{list-style:none;font-family:Arial,sans-serif;font-size:6.2px;color:#fff}
  .footer-list li{height:13.1px}
  .footer-list li::before{content:"•";margin-right:6px}
  .contact-row{display:flex;gap:8px;font-family:Arial,sans-serif;font-size:6.2px;color:#fff;line-height:9px}
  .field{background:#fff;border-radius:2px;font-family:Arial,sans-serif;font-size:6px;color:#666;padding:3px 5px}
  .footer-divider{width:1px;background:#4d5a4d}
  .copyright{left:0;top:1178px;width:686px;height:22px;background:var(--green);color:#fff;font-family:"Lora",serif;font-size:6.5px;text-align:center;line-height:22px}
</style>
</head>
<body>
<div class="page">

  <!-- top bar -->
  <div class="abs topbar"></div>
  <span class="abs social" style="left:290px"></span>
  <span class="abs social" style="left:311px"></span>
  <span class="abs social" style="left:333px"></span>
  <span class="abs social" style="left:355px"></span>
  <div class="abs topbar-contact" style="left:381px">
    <svg width="10" height="7" viewBox="0 0 10 7"><rect x=".5" y=".5" width="9" height="6" fill="none" stroke="#fff"/><path d="M.5 .5 5 4 9.5 .5" fill="none" stroke="#fff"/></svg>
    inquiry@vellorim.com
  </div>
  <div class="abs topbar-contact phone" style="left:508px">
    <svg width="10" height="10" viewBox="0 0 10 10"><circle cx="5" cy="5" r="4.4" fill="none" stroke="#fff"/><path d="M3.6 2.6c-.6.6-.4 2 .6 3.2s2.4 1.5 3 .9l-.8-.9-.7.4-1.4-1.5.4-.7z" fill="#fff"/></svg>
    123-456-7890
  </div>

  <!-- header -->
  <div class="abs header"></div>
  <div class="abs brand" style="left:104px;top:42px">VelLorim</div>
  <nav class="abs nav" style="left:317px">
    <a href="#">Home</a><a href="#">About Us</a><a href="#">Members</a><a href="#">News</a><a href="#">Team</a><a href="#">Contact Us</a>
  </nav>

  <!-- hero -->
  <div class="abs hero" role="img" aria-label="Young seedlings growing out of stacked coins on dark soil"></div>
  <div class="abs hero-title">Pioneering New Growth<br>Opportunities In Uruguay</div>
  <div class="abs hero-arrow" style="left:0"><svg width="6" height="8"><path d="M5 1 2 4l3 3" fill="none" stroke="#fff" stroke-width="1.5"/></svg></div>
  <div class="abs hero-arrow" style="left:664px"><svg width="6" height="8"><path d="M1 1l3 3-3 3" fill="none" stroke="#fff" stroke-width="1.5"/></svg></div>

  <!-- about -->
  <h2 class="abs section-title" style="top:323px">About VelLorim</h2>
  <div class="abs title-rule" style="left:286px;top:350px;width:164px"><span></span></div>
  <p class="abs about-text">VelLorim is a manufacturing startup company in Uruguay, South America. It will grow a specially engineered strain of high CBD hemp, extract and refine the valuable plant oils, and package the oils into therapeutic products. The products will be sold into countries where new markets exist due to deregulation of cannabis (hemp and marijuana), and will target specific diseases known to respond positively to CBD.</p>
  <a class="abs btn" style="left:306px;top:396px;width:73px;height:19px;text-decoration:none">Read More
    <svg width="10" height="6"><path d="M0 3h9M6 .5 9 3 6 5.5" fill="none" stroke="#fff"/></svg></a>

  <!-- cannabidiol -->
  <div class="abs cbd-band"></div>
  <h2 class="abs section-title" style="top:447px">Cannabidiol</h2>
  <div class="abs title-rule" style="left:296px;top:472px;width:94px;background:transparent"><span></span></div>
  <p class="abs cbd-intro">Our hemp was engineered to maximize therapeutic CBD. Under Uruguayan laws we refine the oil at 2x higher profitability than anywhere else in the world.</p>

  <svg class="abs" style="left:0;top:436px" width="686" height="247" viewBox="0 436 686 247">
    <path d="M250 684 A92 92 0 0 1 436 684" fill="#fff" stroke="var(--green-bright)" stroke-width="3.5"/>
    <g fill="#fff" stroke="var(--blue)" stroke-width="1.6">
      <circle cx="255" cy="655" r="3.5"/><circle cx="277" cy="619" r="3.5"/><circle cx="319" cy="595" r="3.5"/>
      <circle cx="366" cy="595" r="3.5"/><circle cx="408" cy="619" r="3.5"/><circle cx="431" cy="655" r="3.5"/>
    </g>
    <g fill="#fff" stroke="var(--blue)" stroke-width="1.6">
      <circle cx="306" cy="555" r="22"/><circle cx="379" cy="555" r="22"/>
      <circle cx="246" cy="585" r="22"/><circle cx="438" cy="585" r="22"/>
      <circle cx="216" cy="641" r="22"/><circle cx="469" cy="641" r="22"/>
    </g>
    <g fill="none" stroke="var(--green)" stroke-width="1.4">
      <!-- therapeutic kit -->
      <rect x="297" y="549" width="18" height="13" rx="1.5"/><path d="M302 549v-3h8v3M306 552v7M302.5 555.5h7"/>
      <!-- cultivation leaf -->
      <path d="M379 564v-4M379 560c-6-2-8-8-8-12 5 1 8 6 8 12zM379 560c6-2 8-8 8-12-5 1-8 6-8 12zM379 560c-2-6 0-11 0-14 0 3 2 8 0 14z"/>
      <!-- globe with lens -->
      <circle cx="244" cy="583" r="9"/><path d="M235 583h18M244 574c-4 5-4 13 0 18M244 574c4 5 4 13 0 18"/><circle cx="250" cy="589" r="4" fill="#fff"/><path d="M253 592l4 4"/>
      <!-- extraction rig -->
      <path d="M438 575v18M433 598l5-23 5 23M431 598h14M434 582h8M433 576c2-3 8-3 10 0"/>
      <!-- genetic gear -->
      <circle cx="219" cy="644" r="6"/><circle cx="219" cy="644" r="2"/><path d="M219 636v2M219 650v2M211 644h2M225 644h2M213 638l1.5 1.5M223.5 648.5 225 650M213 650l1.5-1.5M223.5 639.5 225 638M207 634l8 4M206 640l6-2"/>
      <!-- refinery bars -->
      <path d="M459 652h20M461 652v-8h4v8M466 652v-13h4v13M471 652v-10h4v10M475 652v-16h3v16"/>
    </g>
  </svg>

  <div class="abs feature right" style="left:150px;top:535px;width:128px">Therpeutic Products</div>
  <div class="abs feature" style="left:409px;top:535px">Hemp Cultivation</div>
  <div class="abs feature right" style="left:100px;top:575px;width:117px">New Markets</div>
  <div class="abs feature" style="left:474px;top:575px">Extraction</div>
  <div class="abs feature right" style="left:60px;top:635px;width:125px">Genetic Engineering</div>
  <div class="abs feature" style="left:501px;top:635px">Oil Refinement</div>
  <div class="abs cbd-brand">VelLorim</div>
  <div class="abs cbd-sub">CBD</div>

  <!-- latest news -->
  <h2 class="abs section-title" style="top:707px">Latest News</h2>
  <div class="abs title-rule" style="left:282px;top:733px;width:108px;background:transparent"><span></span></div>

  <div class="abs news-thumb" style="left:92px;top:746px;background:linear-gradient(135deg,#f0ead0,#c9d9a6)" role="img" aria-label="Poster of hands holding a hemp plant"></div>
  <div class="abs news-title" style="left:178px;top:745px">Lorem ipsum dolor sit amet nonumy nibh</div>
  <div class="abs news-date" style="left:178px;top:760px">
    <svg width="7" height="7"><rect x=".5" y="1" width="6" height="5.5" fill="none" stroke="#2a63b0"/><path d="M.5 3h6" stroke="#2a63b0"/></svg>07, FEB-2017</div>
  <p class="abs news-body" style="left:178px;top:771px">Duis aute eummutation ullamcorper suscipit lobortismi nisl ut aliquip ex ea commodo consequat. Duis autem ok vel eummu &nbsp;iriure facilis &nbsp;<b>...[+]</b></p>

  <div class="abs footer-divider" style="left:342px;top:748px;height:50px;background:#e4e4e4"></div>

  <div class="abs news-thumb" style="left:358px;top:746px;background:linear-gradient(135deg,#e4e4e0,#cfd4c4)" role="img" aria-label="Hemp nutrition poster with figures"></div>
  <div class="abs news-title" style="left:444px;top:745px">Lorem ipsum dolor sit amet nonumy nibh</div>
  <div class="abs news-date" style="left:444px;top:760px">
    <svg width="7" height="7"><rect x=".5" y="1" width="6" height="5.5" fill="none" stroke="#2a63b0"/><path d="M.5 3h6" stroke="#2a63b0"/></svg>07, FEB-2017</div>
  <p class="abs news-body" style="left:444px;top:771px">Duis aute eummutation ullamcorper suscipit lobortismi nisl ut aliquip ex ea commodo consequat. Duis autem ok vel eummu &nbsp;iriure facilis &nbsp;<b>...[+]</b></p>

  <!-- team -->
  <div class="abs team-band"></div>
  <h2 class="abs section-title" style="top:838px">Our Team</h2>
  <div class="abs title-rule" style="left:294px;top:864px;width:98px;background:transparent"><span></span></div>

  <div class="abs member" style="left:93px"><div class="member-photo" style="background:linear-gradient(160deg,#d9d5cf,#8b8580)" role="img" aria-label="Portrait of a team member"></div><div class="member-name">Lorem ipsum do</div></div>
  <div class="abs member" style="left:177px"><div class="member-photo" style="background:linear-gradient(160deg,#9fb58a,#4d5d3a)" role="img" aria-label="Team member inspecting hemp plants"></div><div class="member-name">Lorem ipsum do</div></div>
  <div class="abs member" style="left:262px"><div class="member-photo" style="background:linear-gradient(160deg,#a58f7a,#5d4a3b)" role="img" aria-label="Portrait of a team member"></div><div class="member-name">Lorem ipsum do</div></div>
  <div class="abs member" style="left:346px"><div class="member-photo" style="background:linear-gradient(160deg,#7ea85c,#3b5a2a)" role="img" aria-label="Team member in a hemp field"></div><div class="member-name">Lorem ipsum do</div></div>
  <div class="abs member" style="left:430px"><div class="member-photo" style="background:linear-gradient(160deg,#6e6050,#2d2620)" role="img" aria-label="Portrait of a team member in an office"></div><div class="member-name">Lorem ipsum do</div></div>
  <div class="abs member" style="left:514px"><div class="member-photo" style="background:linear-gradient(160deg,#eef0f1,#9ea3a6)" role="img" aria-label="Portrait of a team member"></div><div class="member-name">Lorem ipsum do</div></div>

  <!-- call to action -->
  <div class="abs cta"></div>
  <p class="abs cta-text">VelLorim is not just designing CBD products, it is designed to<br>maximize investor returns.</p>
  <div class="abs cta-btn"><div style="font-size:7.5px;margin-top:3px">Call Us Today</div><div style="font-size:11.5px;line-height:13px">123-456-7890</div></div>

  <!-- footer -->
  <div class="abs footer" role="img" aria-label="Dark, softly blurred hemp leaves"></div>

  <div class="abs" style="left:94px;top:1047px;width:60px">
    <div class="footer-head">Quick Link</div>
    <ul class="footer-list" style="margin-top:9px">
      <li>Home</li><li>About Us</li><li>Members</li><li>News</li><li>Team</li><li>Contact Us</li>
    </ul>
  </div>
  <div class="abs footer-divider" style="left:172px;top:1050px;height:112px"></div>

  <div class="abs" style="left:194px;top:1047px;width:104px">
    <div class="footer-head">Contact Details</div>
    <div class="contact-row" style="margin-top:9px">
      <svg width="6" height="8"><path d="M3 7.5C1 5 .5 4 .5 3a2.5 2.5 0 0 1 5 0c0 1-.5 2-2.5 4.5z" fill="#fff"/><circle cx="3" cy="3" r="1" fill="#1c2a1c"/></svg>
      <div>VelLorim<br>Street Name, City Name<br>State Zipcode</div>
    </div>
    <div class="contact-row" style="margin-top:6px">
      <svg width="7" height="7"><path d="M1.5 .5c-1 1-.8 3 .8 4.6s3.5 1.8 4.4.9l-1.2-1.3-1 .6-2-2.2.6-1z" fill="#fff"/></svg>123-456-7890</div>
    <div class="contact-row" style="margin-top:6px">
      <svg width="7" height="7"><rect x="1.5" y=".5" width="4" height="2" fill="#fff"/><rect x=".5" y="2.5" width="6" height="3" fill="#fff"/><rect x="1.5" y="5" width="4" height="1.5" fill="#fff"/></svg>123-456-7890</div>
    <div class="contact-row" style="margin-top:6px">
      <svg width="7" height="6"><rect x=".5" y=".5" width="6" height="4.5" fill="none" stroke="#fff"/><path d="M.5 .5 3.5 3l3-2.5" fill="none" stroke="#fff"/></svg>inquiry@vellorim.com</div>
  </div>
  <div class="abs footer-divider" style="left:316px;top:1050px;height:112px"></div>

  <div class="abs" style="left:338px;top:1047px;width:120px">
    <div class="footer-head">Quick Inquiry</div>
  </div>
  <div class="abs field" style="left:338px;top:1072px;width:120px;height:15px">Name</div>
  <div class="abs field" style="left:338px;top:1090px;width:120px;height:15px;padding-top:7px">Email</div>
  <div class="abs field" style="left:338px;top:1107px;width:120px;height:31px">Message</div>
  <div class="abs btn" style="left:338px;top:1142px;width:60px;height:18px">Submit
    <svg width="10" height="6"><path d="M0 3h9M6 .5 9 3 6 5.5" fill="none" stroke="#fff"/></svg></div>

  <div class="abs brand" style="left:498px;top:1101px;font-size:20px;color:#3d7ed0">VelLorim</div>

  <div class="abs copyright">Copyright © 2017 VelLorim. All Rights Reserved.</div>
</div>
</body>
</html>
```